BRIM Outreach Partners Business Card Rebrand

Hello Designers! We are looking for help designing our new business card to go in conjunction with our company rebrand. Unfortunately, we have an event mid June that requires we get these printed ASAP (before our new website is launched.) We have a mostly complete Brand Book which I have uploaded to this request for your reference to company information, style, fonts. I've also enclosed our logo file in .eps & .jpg. Attached is a sample business card my boss liked but said was "too simple." I made it in Canva and do not profess to be a designer. NOT FOR DESIGN REFERENCE, ONLY FOR CONTEXT Here is what our old website looks like: https://brimoutreachpartners.com/.

```html
<!DOCTYPE html>
<html lang="en">
<head>
<meta charset="utf-8">
<title>BRIM Outreach Partners – Business Card</title>
<link rel="stylesheet" href="https://fonts.googleapis.com/css2?family=Oxygen:wght@400;700&display=swap">
<style>
  :root {
    --backdrop: #8f8f8f;
    --card-white: #ffffff;
    --card-black: #000000;
    --brand-blue: #4db4e6;
    --ink: #1a1a1a;
    --logo-grey: #dcdcdc;
  }
  * { box-sizing: border-box; margin: 0; padding: 0; }
  html, body {
    width: 1200px; height: 1200px; overflow: hidden;
    background: var(--backdrop);
    font-family: "Oxygen", sans-serif;
  }
  .canvas { position: relative; width: 1200px; height: 1200px; }
  .card {
    position: absolute; left: 281px; width: 641px; height: 365px;
    border-radius: 32px; overflow: hidden;
  }
  .card--front { top: 195px; background: var(--card-white); }
  .card--back { top: 639px; background: var(--card-black); }

  .front-accent {
    position: absolute; left: -61px; top: 13px;
    width: 340px; height: 340px; border-radius: 50%;
    background: var(--brand-blue);
  }

  .contact-block {
    position: absolute; right: 38px; top: 178px; text-align: right; color: var(--ink);
  }
  .person-name {
    font-weight: 700; font-size: 26px; letter-spacing: 0.2px; line-height: 1;
  }
  .person-title { font-size: 15.5px; margin-top: 10px; line-height: 1; }
  .contact-list { list-style: none; margin-top: 20px; }
  .contact-item {
    display: flex; justify-content: flex-end; align-items: center;
    font-size: 14px; height: 22.5px; letter-spacing: 0.2px;
  }
  .contact-icon { width: 12px; height: 12px; margin-left: 11px; fill: var(--ink); }

  .brand-lockup {
    position: absolute; left: 121px; top: 115px;
    display: flex; align-items: center; gap: 18px;
  }
  .brand-mark {
    width: 136px; height: 136px; border-radius: 50%; background: var(--brand-blue); flex: none;
  }
  .brand-name {
    color: var(--logo-grey); font-weight: 700; font-size: 30px; line-height: 1.1; width: 260px;
  }
</style>
</head>
<body>
<main class="canvas">
  <section class="card card--front" aria-label="Business card front">
    <div class="front-accent" aria-hidden="true"></div>
    <div class="contact-block">
      <h1 class="person-name">DANIEL MORROW-HALE</h1>
      <p class="person-title">Managing Partner</p>
      <ul class="contact-list">
        <li class="contact-item">+1-555-014-2297
          <svg class="contact-icon" viewBox="0 0 12 12" aria-hidden="true"><path d="M3 0h6a1 1 0 0 1 1 1v10a1 1 0 0 1-1 1H3a1 1 0 0 1-1-1V1a1 1 0 0 1 1-1zm0.5 1.5v8h5v-8zM6 10.2a.6.6 0 1 0 0 1.2.6.6 0 0 0 0-1.2z"/></svg>
        </li>
        <li class="contact-item">daniel@brimoutreachpartners.com
          <svg class="contact-icon" viewBox="0 0 12 12" aria-hidden="true"><path d="M0 2.5h12v1L6 7 0 3.5zM0 5l6 3.5L12 5v4.5H0z"/></svg>
        </li>
        <li class="contact-item">www.brimoutreachpartners.com
          <svg class="contact-icon" viewBox="0 0 12 12" aria-hidden="true"><circle cx="6" cy="6" r="5.5"/><path d="M3 3.5c1 0 2 .5 2 1.5S4 6 4 7s1 1.5 1 2.5M8 2.5c-.5 1 .5 1.5 1.5 2" stroke="#fff" stroke-width="1" fill="none"/></svg>
        </li>
        <li class="contact-item">Denver, CO Based (Mountain Time)
          <svg class="contact-icon" viewBox="0 0 12 12" aria-hidden="true"><path d="M6 0a4 4 0 0 1 4 4c0 3-4 8-4 8S2 7 2 4a4 4 0 0 1 4-4zm0 2.3a1.7 1.7 0 1 0 0 3.4 1.7 1.7 0 0 0 0-3.4z"/></svg>
        </li>
      </ul>
    </div>
  </section>

  <section class="card card--back" aria-label="Business card back">
    <div class="brand-lockup">
      <span class="brand-mark" aria-hidden="true"></span>
      <p class="brand-name">BRIM Outreach Partners</p>
    </div>
  </section>
</main>
</body>
</html>
```